Refresh Application User Interface

Brindlecove wishes to update the look of its business applications. Two representative forms are shown below. Please note, we are not considering changes in functionality or usability. Our goal is a cleaner, more contemporary design.

Industry/Entity Type

Business

```html
<!DOCTYPE html>
<html lang="en">
<head>
<meta charset="utf-8">
<title>Brindlecove – Purchase Order</title>
<link href="https://fonts.googleapis.com/css2?family=Lato:wght@400;700;900&display=swap" rel="stylesheet">
<style>
:root{
  --navy:#0f326e;
  --navy-2:#1d4f9a;
  --blue-link:#1d58a8;
  --green:#3c9f10;
  --green-light:#52b81a;
  --green-text:#3aa60c;
  --page:#ebebeb;
  --nav-bg:#f2f2f2;
  --field-border:#bfbfbf;
  --text:#1b1b1b;
  --muted:#555;
  --orange:#f5a000;
}
*{box-sizing:border-box;margin:0;padding:0}
html,body{width:1200px;height:1160px;overflow:hidden}
body{background:var(--page);font-family:'Lato',sans-serif;color:var(--text);position:relative}
.abs{position:absolute}
a{color:inherit;text-decoration:none}

/* top bar */
.topbar{position:absolute;left:0;top:0;width:1200px;height:40px;background:var(--navy);color:#fff;font-size:14px}
.topbar .user{left:114px;top:10px}
.topbar .role{left:325px;top:10px}
.topbar .links{right:70px;top:0;height:40px;display:flex}
.topbar .links a{padding:0 11px;line-height:40px;border-left:1px solid rgba(255,255,255,.25)}
.topbar .links a:first-child{border-left:0}

/* main nav */
.mainnav{position:absolute;left:0;top:40px;width:1200px;height:80px;background:var(--nav-bg)}
.mainnav .item{position:absolute;top:0;height:80px;line-height:88px;font-weight:900;font-size:15px;color:var(--navy)}
.mainnav .item.active{background:var(--green-light);color:#fff;padding:0 11px;margin-left:-15px}
.brand{position:absolute;left:912px;top:29px;width:189px;height:30px;background:#fff;display:flex;align-items:center;justify-content:center;gap:8px;font-weight:900;font-size:22px;color:var(--navy)}
.brand .dot{width:12px;height:12px;border-radius:50%;background:var(--green-light)}

/* sub nav */
.subnav{position:absolute;left:0;top:120px;width:1200px;height:49px;background:linear-gradient(#45aa15,#379a0e);color:#fff;font-size:15px}
.subnav span{position:absolute;top:15px}
.subnav .pill{left:126px;top:11px;width:80px;height:28px;border-radius:14px;background:var(--navy);text-align:center;line-height:28px}

/* page heading + tabs */
.title{left:110px;top:202px;font-size:27px;color:var(--navy);font-weight:400}
.sectiontabs{left:766px;top:218px;height:36px;display:flex;font-size:14px;color:#222}
.sectiontabs span{position:relative;padding:0 14px;line-height:40px}
.sectiontabs .on{background:var(--navy-2);color:#fff;width:93px;text-align:center}
.sectiontabs .check{position:absolute;right:-2px;top:4px}

/* toolbar */
.toolbar{position:absolute;left:110px;top:254px;width:980px;height:54px;background:linear-gradient(#2c5fa8,#163f86);color:#fff}
.toolbar .ico{position:absolute;top:0;height:54px;display:flex;align-items:center;justify-content:center;border-right:1px solid rgba(255,255,255,.2)}
.toolbar .post{left:266px;top:17px;font-size:17px;display:flex;align-items:center;gap:6px}
.toolbar .actions{right:28px;top:0;height:54px;display:flex;align-items:center;gap:18px;font-size:14px}
.toolbar .actions span{display:flex;align-items:center;gap:4px}

/* panel */
.panel{position:absolute;left:110px;top:308px;width:980px;height:737px;background:#fff;box-shadow:0 1px 3px rgba(0,0,0,.2)}
.lbl{position:absolute;font-size:16px;text-align:right;color:var(--text)}
.field{position:absolute;height:28px;border:1px solid var(--field-border);background:#fff;font-size:13px;padding-left:8px;line-height:26px;color:#333}
.select::after{content:"";position:absolute;right:14px;top:8px;width:7px;height:7px;border-right:1px solid #777;border-bottom:1px solid #777;transform:rotate(45deg)}
.sel{height:29px;line-height:27px;padding-left:13px;color:#555}

/* inner tab box */
.tabbox{position:absolute;left:24px;top:280px;width:923px;height:394px;background:#fff;box-shadow:0 1px 3px rgba(0,0,0,.3)}
.tabbar{position:absolute;left:0;top:0;width:923px;height:46px;background:linear-gradient(#48ad16,#379a0e);color:#fff;font-size:16px}
.tabbar span{position:absolute;top:15px}
.tabbar .on{left:112px;top:0;width:98px;height:46px;line-height:60px;background:#2c8a08;text-align:center}

.hint{left:0;width:980px;text-align:center;top:694px;font-size:17px;color:var(--blue-link)}
.footer-line{left:110px;top:1094px;width:980px;height:1px;background:#9a9a9a}
.footer{left:0;width:1200px;text-align:center;top:1114px;font-size:14px;color:var(--muted)}
.pageid{left:1140px;top:1132px;font-size:13px;color:var(--muted)}
</style>
</head>
<body>

<header class="topbar">
  <div class="abs user">Logged in As Dana Keller
    <svg width="14" height="14" viewBox="0 0 24 24" style="vertical-align:-2px"><circle cx="12" cy="12" r="8" fill="none" stroke="#fff" stroke-width="5" stroke-dasharray="4 2.3"/><circle cx="12" cy="12" r="4" fill="#fff"/></svg>
  </div>
  <div class="abs role">Current Role: Administrator
    <svg width="10" height="14" viewBox="0 0 10 14" style="vertical-align:-2px"><path d="M2 1l6 6-6 6" fill="none" stroke="#fff" stroke-width="2.5"/></svg>
  </div>
  <nav class="abs links"><a>Touch</a><a>News Tab</a><a>Help</a><a>Support</a><a>Log Out</a></nav>
</header>

<nav class="mainnav">
  <a class="item" style="left:129px">HOME</a>
  <a class="item active" style="left:208px;padding:0 16px 0 16px">ESOURCE</a>
  <a class="item" style="left:310px">EBUY</a>
  <a class="item" style="left:383px">EREQUEST</a>
  <a class="item" style="left:491px">ESELL</a>
  <a class="item" style="left:567px">ESTOCK</a>
  <a class="item" style="left:658px">EPLAN</a>
  <a class="item" style="left:740px">PREFRENCES</a>
  <div class="brand"><span>Brindlecove</span><span class="dot"></span></div>
</nav>

<nav class="subnav">
  <span class="pill">Orders</span>
  <span style="left:226px">Requests</span>
  <span style="left:317px">Shipments</span>
  <span style="left:418px">Invoice</span>
  <span style="left:495px">Pricing</span>
  <span style="left:572px">Tables</span>
  <span style="left:643px">Reports</span>
  <span style="left:728px">Inquiries</span>
  <span style="left:817px">Periodic Tasks</span>
  <span style="left:942px">Workflows</span>
</nav>

<h1 class="abs title">Purchase Order</h1>
<div class="abs sectiontabs">
  <span class="on">HEADER</span>
  <span>LINES<svg class="check" width="14" height="14" viewBox="0 0 14 14"><circle cx="7" cy="7" r="6" fill="none" stroke="#3aa60c" stroke-width="1.3"/><path d="M4 7l2 2 4-4" fill="none" stroke="#3aa60c" stroke-width="1.3"/></svg></span>
  <span>CHARGES</span>
  <span>NOTES<svg class="check" width="14" height="14" viewBox="0 0 14 14"><circle cx="7" cy="7" r="6" fill="none" stroke="#3aa60c" stroke-width="1.3"/><path d="M4 7l2 2 4-4" fill="none" stroke="#3aa60c" stroke-width="1.3"/></svg></span>
</div>

<div class="toolbar">
  <div class="ico" style="left:0;width:56px"><svg width="26" height="26" viewBox="0 0 24 24"><path d="M8 14l7-7a3 3 0 014 4l-9 9a5 5 0 01-7-7l8-8" fill="none" stroke="#fff" stroke-width="2"/></svg></div>
  <div class="ico" style="left:56px;width:50px"><svg width="26" height="26" viewBox="0 0 24 24"><path d="M6 2h9l5 5v15H6V2z M15 2v5h5" fill="none" stroke="#fff" stroke-width="1.6"/><circle cx="9" cy="16" r="3" fill="none" stroke="#fff" stroke-width="1.6"/><path d="M7 18l-3 3" stroke="#fff" stroke-width="1.6"/></svg></div>
  <div class="ico" style="left:106px;width:54px"><svg width="26" height="26" viewBox="0 0 24 24"><circle cx="5" cy="5" r="3" fill="#fff"/><circle cx="19" cy="5" r="3" fill="#fff"/><circle cx="5" cy="19" r="3" fill="#fff"/><circle cx="19" cy="19" r="3" fill="#fff"/><path d="M5 5v14M5 5l14 14M19 5v14" stroke="#fff" stroke-width="2"/></svg></div>
  <div class="ico" style="left:160px;width:52px"><svg width="26" height="24" viewBox="0 0 24 22"><rect x="1" y="2" width="22" height="5" fill="none" stroke="#fff" stroke-width="1.6"/><path d="M3 7v13h18V7M9 11h6" fill="none" stroke="#fff" stroke-width="1.6"/></svg></div>
  <div class="ico" style="left:212px;width:42px"><svg width="24" height="24" viewBox="0 0 24 24"><circle cx="12" cy="12" r="11" fill="#fff"/><text x="12" y="17" text-anchor="middle" font-family="Lato,sans-serif" font-weight="900" font-size="15" fill="#1d4f9a">?</text></svg></div>
  <div class="abs post"><svg width="24" height="26" viewBox="0 0 24 26"><path d="M3 1h10l5 5v6 M3 1v23h9" fill="none" stroke="#fff" stroke-width="1.6"/><circle cx="16" cy="18" r="6" fill="none" stroke="#fff" stroke-width="1.6"/><path d="M16 15v6M13 18h6" stroke="#fff" stroke-width="1.6"/></svg>Post Order</div>
  <div class="abs actions">
    <span><svg width="14" height="14" viewBox="0 0 14 14"><circle cx="6" cy="6" r="4.3" fill="none" stroke="#fff" stroke-width="2"/><path d="M9 9l4 4" stroke="#fff" stroke-width="2"/></svg>SEARCH</span>
    <span><svg width="18" height="16" viewBox="0 0 18 16"><rect x="1" y="1" width="16" height="14" fill="none" stroke="#fff" stroke-width="1.4"/><path d="M4 5h10M4 8h10M4 11h10" stroke="#fff" stroke-width="1.4"/></svg>NEWS</span>
    <span><svg width="18" height="18" viewBox="0 0 18 18"><circle cx="9" cy="9" r="8" fill="none" stroke="#fff" stroke-width="1.4"/><path d="M5 9l3 3 5-6" fill="none" stroke="#fff" stroke-width="1.6"/></svg>APPLY</span>
    <span><svg width="18" height="18" viewBox="0 0 18 18"><rect x="1" y="1" width="16" height="16" fill="none" stroke="#fff" stroke-width="1.4"/><path d="M5 5l8 8M13 5l-8 8" stroke="#fff" stroke-width="1.6"/></svg>DELETE</span>
    <span><svg width="18" height="18" viewBox="0 0 18 18"><circle cx="9" cy="9" r="8" fill="none" stroke="#fff" stroke-width="1.4"/><path d="M13 9H5M8 6L5 9l3 3" fill="none" stroke="#fff" stroke-width="1.6"/></svg>BACK</span>
  </div>
</div>

<main class="panel">
  <div class="lbl" style="left:40px;width:82px;top:37px">Order#</div>
  <div class="abs" style="left:161px;top:38px;font-size:14px">100159</div>
  <div class="abs" style="left:332px;top:38px;font-size:15px;color:var(--green-text)">Regular Purchase Order</div>
  <div class="abs" style="left:798px;top:24px;font-size:15px;color:var(--blue-link)">Hold for Completion</div>

  <div class="lbl" style="left:40px;width:82px;top:73px">Ship From</div>
  <div class="field" style="left:153px;top:68px;width:124px">1001</div>
  <div class="field" style="left:281px;top:68px;width:52px">/0</div>
  <div class="field" style="left:153px;top:105px;width:361px">Harborline Medical Inc</div>
  <svg class="abs" style="left:521px;top:102px" width="26" height="26" viewBox="0 0 26 26"><circle cx="13" cy="13" r="12" fill="#d9a92a"/></svg>

  <div class="lbl" style="left:40px;width:82px;top:145px">Address</div>
  <div class="field" style="left:153px;top:141px;width:361px">14 Tidewater Rd</div>
  <div class="lbl" style="left:40px;width:82px;top:181px">City</div>
  <div class="field" style="left:153px;top:177px;width:361px">Linwood Falls</div>
  <div class="lbl" style="left:40px;width:82px;top:218px">Zip</div>
  <div class="field" style="left:153px;top:213px;width:361px">04821-1190</div>

  <div class="abs" style="left:542px;top:148px;font-size:16px">DPV Unconfirmed</div>
  <div class="abs" style="left:682px;top:137px;width:19px;height:19px;border:1px solid var(--field-border)"></div>
  <div class="abs" style="left:710px;top:138px;font-size:15px;color:var(--muted)">Accept</div>

  <div class="lbl" style="left:530px;width:72px;top:180px">State</div>
  <div class="field" style="left:606px;top:175px;width:182px"></div>
  <div class="lbl" style="left:530px;width:72px;top:216px">Country</div>
  <div class="field" style="left:606px;top:210px;width:182px">US</div>
  <div class="abs" style="left:867px;top:226px;font-size:15px;color:var(--green-text);text-decoration:underline">Add Contact</div>

  <section class="tabbox">
    <div class="tabbar">
      <span style="left:28px">Order Info</span>
      <span class="on">Shipping</span>
      <span style="left:218px">Payment</span>
      <span style="left:307px">Accounts</span>
      <span style="left:400px">Total/ Approval</span>
    </div>

    <div class="lbl" style="left:20px;width:139px;top:83px">Receive At</div>
    <div class="field select sel" style="left:183px;top:77px;width:191px">ALCH</div>
    <div class="lbl" style="left:20px;width:139px;top:119px">Carrier</div>
    <div class="field select sel" style="left:183px;top:113px;width:191px">Swiftline</div>
    <div class="lbl" style="left:20px;width:139px;top:156px">Express Service</div>
    <div class="field select sel" style="left:183px;top:149px;width:191px"></div>
    <div class="lbl" style="left:20px;width:139px;top:192px">FOB</div>
    <div class="field select sel" style="left:183px;top:185px;width:191px"></div>
    <div class="lbl" style="left:20px;width:139px;top:228px">Order Ship Rule</div>
    <div class="field select sel" style="left:183px;top:222px;width:191px">Partials</div>
    <div class="lbl" style="left:20px;width:139px;top:265px">Line Ship Rule</div>
    <div class="field select sel" style="left:183px;top:260px;width:191px">Partials</div>

    <div class="lbl" style="left:400px;width:146px;top:88px">Request Date</div>
    <div class="field sel" style="left:568px;top:77px;width:191px">01/07/2018
      <svg class="abs" style="right:10px;top:5px" width="18" height="17" viewBox="0 0 18 17"><rect x="1" y="2" width="16" height="14" fill="none" stroke="#777" stroke-width="1.2"/><path d="M1 6h16M5 0v4M13 0v4M5 9h2M9 9h2M13 9h1M5 12h2M9 12h2M13 12h1" stroke="#777" stroke-width="1.2"/></svg>
    </div>
    <div class="lbl" style="left:400px;width:146px;top:122px">Freight Terms</div>
    <div class="field select sel" style="left:568px;top:118px;width:191px">Collect</div>
    <div class="lbl" style="left:400px;width:146px;top:159px">Freight Calc</div>
    <div class="field select sel" style="left:568px;top:156px;width:191px"></div>
    <div class="lbl" style="left:400px;width:146px;top:239px">Customer Ship To</div>
    <div class="field" style="left:568px;top:229px;width:127px;height:29px"></div>
    <div class="abs" style="left:702px;top:233px;font-size:16px;color:#666">/</div>
    <div class="field" style="left:714px;top:229px;width:46px;height:29px"></div>

    <svg class="abs" style="left:857px;top:326px" width="18" height="22" viewBox="0 0 18 22"><path d="M4 10V6a5 5 0 0110 0v4" fill="none" stroke="#f5a000" stroke-width="2.5"/><rect x="1" y="10" width="16" height="12" rx="1" fill="#f5a000"/></svg>
  </section>

  <div class="abs hint">Enter Property Value, and Click Apply</div>
</main>

<div class="abs footer-line"></div>
<div class="abs footer">© 2018 Company Name &nbsp;All right reserved &nbsp;Terms of Use</div>
<div class="abs pageid">X14</div>

</body>
</html>
```